b2c portal. NomiDeals. Attract diners and drinkers to restaurant/bar deals

aggregator site for restaurants and bars to promote their deals/discounts

1. we are an aggregator portal that lists all deals and discounts (Happy Hour, etc.) for restaurants and bars. the layout is similar to Quorbi and RoamVista, without the ratings.
2. the target market is identical to Quorbi and those searching for restaurants on RoamVista.
3. I have attached a file of a preliminary screenshot of a home page.

Target Market(s)

all guests of restaurants and bars

Number of Pages Required

4 page

Requirements
Must have
• a good story loop.
see Quorbi, RoamVista, FlinkDine
Should not have
• keep it simple

```html
<!DOCTYPE html>
<html lang="en">
<head>
<meta charset="utf-8">
<title>NomiDeals — Find Restaurant Offers</title>
<link href="https://fonts.googleapis.com/css2?family=Catamaran:wght@400;500;600&family=Poppins:wght@400;500;600&family=Alegreya:ital@1&display=swap" rel="stylesheet">
<style>
:root{
  --teal:#2f7b7a;
  --orange:#d1692b;
  --ink:#2b2b2b;
  --muted:#5d5d5d;
  --page:#f6f6f6;
  --card:#ffffff;
  --footer:#414141;
  --footer-bar:#3a3a3a;
  --footer-text:#d6d6d6;
}
*{box-sizing:border-box;margin:0;padding:0}
html,body{width:1200px;height:2970px;overflow:hidden}
body{position:relative;background:var(--page);font-family:"Catamaran",sans-serif;color:var(--ink)}
.abs{position:absolute}

/* header */
.topbar{left:0;top:0;width:1200px;height:66px;background:var(--page)}
.brand{left:120px;top:10px;font-family:"Catamaran",sans-serif;font-weight:600;font-size:42px;color:var(--orange);letter-spacing:-0.5px;line-height:48px}
.btn{height:38px;width:94px;border-radius:3px;font-family:"Catamaran",sans-serif;font-size:16px;display:flex;align-items:center;justify-content:center;top:15px}
.btn-outline{left:880px;border:1px solid var(--teal);color:var(--ink);background:#fff}
.btn-solid{left:986px;background:var(--teal);color:#fff}

/* hero */
.hero{left:0;top:66px;width:1200px;height:626px;background:radial-gradient(ellipse at 30% 30%,#8a5a2c 0%,#4a2d18 45%,#25170d 100%)}
.hero-shade{left:0;top:66px;width:1200px;height:626px;background:linear-gradient(90deg,rgba(0,0,0,.15),rgba(0,0,0,0) 40%,rgba(0,0,0,.2))}
.nav-item{color:#fff;font-size:20px;top:110px;line-height:28px}
.nav-icon{top:76px}
.nav-div{width:1px;background:rgba(255,255,255,.45)}
.hero-title{left:0;width:1200px;top:295px;text-align:center;font-family:"Alegreya",serif;font-style:italic;font-size:58px;color:#fff;line-height:70px}
.hero-sub{left:0;width:1200px;top:378px;text-align:center;font-family:"Alegreya",serif;font-style:italic;font-size:28px;color:#fff}
.search{left:326px;top:458px;width:548px;height:40px;background:#fff;border-radius:20px;overflow:hidden;display:flex}
.search .field{width:251px;padding-left:26px;line-height:40px;font-size:17px;color:#777}
.search .field + .field{border-left:1px solid #ccc;padding-left:14px;width:239px}
.search .go{margin-left:auto;width:58px;background:#111;display:flex;align-items:center;justify-content:center}

/* section headings */
.h-section{left:0;width:1200px;text-align:center;font-size:40px;font-weight:500;letter-spacing:-1.4px;color:#222;line-height:46px}

/* category cards */
.cat{width:245px;height:244px;background:var(--card);box-shadow:0 1px 4px rgba(0,0,0,.06);top:854px}
.cat .photo{width:245px;height:184px}
.cat .label{text-align:center;font-size:21px;line-height:60px;color:#222}
.dot{top:1133px;width:11px;height:11px;border-radius:50%;border:1px solid #888}
.dot.on{width:15px;height:15px;top:1131px;background:var(--teal);border:none}

/* restaurant cards */
.rest{width:277px;height:339px;background:var(--card);box-shadow:0 1px 5px rgba(0,0,0,.07)}
.rest .photo{position:absolute;left:8px;top:8px;width:261px;height:184px}
.rest .fav{position:absolute;right:17px;top:17px;width:30px;height:30px;border-radius:50%;background:rgba(0,0,0,.45);display:flex;align-items:center;justify-content:center}
.rest .name{position:absolute;left:15px;top:206px;font-size:19px;color:#222}
.rest .desc{position:absolute;left:15px;top:240px;font-size:15px;line-height:19px;color:var(--muted);width:240px}
.rest .opened{position:absolute;left:18px;top:297px;font-size:14px;color:var(--orange)}

/* blog */
.post{width:278px}
.post .photo{position:relative;width:278px;height:176px;border-radius:3px}
.post .date{position:absolute;left:8px;top:8px;width:48px;height:48px;border-radius:50%;background:#fff;font-family:"Poppins",sans-serif;font-size:10px;font-weight:500;line-height:11px;text-align:center;padding-top:14px;color:#222}
.post .meta{margin-top:20px;font-size:13px;color:var(--teal)}
.post .meta span{margin-left:22px}
.post .title{margin-top:4px;font-size:20px;line-height:24px;color:#222}
.post .excerpt{margin-top:9px;font-size:15px;line-height:23px;color:var(--muted)}
.post .more{display:inline-block;margin-top:8px;font-size:15px;color:var(--orange);text-decoration:underline}

/* footer */
.footer{left:0;top:2606px;width:1200px;height:300px;background:var(--footer)}
.footer-bar{left:0;top:2906px;width:1200px;height:64px;background:var(--footer-bar);border-top:1px solid #555}
.f-brand{left:120px;top:2740px;font-weight:600;font-size:48px;color:#fff;letter-spacing:-0.5px;line-height:54px}
.social{top:2834px;width:18px;height:18px;border-radius:50%;background:#fff}
.f-head{font-family:"Poppins",sans-serif;font-size:15px;font-weight:500;color:#fff}
.f-text{font-family:"Poppins",sans-serif;font-size:13px;color:var(--footer-text);line-height:21px}
.f-links{font-family:"Poppins",sans-serif;font-size:13px;color:var(--footer-text);line-height:22.5px;list-style:none}
.cta{left:806px;top:2824px;width:175px;height:44px;background:var(--teal);color:#fff;font-family:"Poppins",sans-serif;font-size:17px;display:flex;align-items:center;justify-content:center;gap:8px;border-radius:2px}
.copy{left:120px;top:2925px;font-family:"Poppins",sans-serif;font-size:14px;color:var(--footer-text)}
.legal{top:2927px;font-family:"Poppins",sans-serif;font-size:13px;color:var(--footer-text)}
</style>
</head>
<body>

<!-- header -->
<div class="abs topbar"></div>
<div class="abs brand">NomiDeals</div>
<div class="abs btn btn-outline">Sign In</div>
<div class="abs btn btn-solid">Sign In</div>

<!-- hero -->
<div class="abs hero" role="img" aria-label="Blurred restaurant scene with guests raising champagne glasses in a toast"></div>
<div class="abs hero-shade"></div>

<svg class="abs nav-icon" style="left:178px" width="30" height="32" viewBox="0 0 30 32" fill="none" stroke="#fff" stroke-width="1.5" stroke-linecap="round">
  <path d="M6 3h7l-1 9a3 3 0 0 1-5 0z"/><path d="M9.5 14v12M6 27h7"/>
  <path d="M17 3h7l-1 9a3 3 0 0 1-5 0z"/><path d="M20.5 14v12M17 27h7"/>
</svg>
<div class="abs nav-item" style="left:120px">Diners &amp; Drinkers</div>
<div class="abs nav-div" style="left:292px;top:84px;height:52px"></div>
<svg class="abs nav-icon" style="left:356px" width="32" height="32" viewBox="0 0 32 32" fill="none" stroke="#fff" stroke-width="1.5" stroke-linecap="round">
  <circle cx="16" cy="6" r="1.6"/><path d="M5 21a11 11 0 0 1 22 0z"/><path d="M3 24h26"/><path d="M10 17a6 6 0 0 1 4-4"/>
</svg>
<div class="abs nav-item" style="left:316px">Restaurant/Bar</div>

<div class="abs nav-item" style="left:925px">Blog</div>
<div class="abs nav-div" style="left:986px;top:114px;height:22px"></div>
<div class="abs nav-item" style="left:1010px">Contact</div>

<div class="abs hero-title">Find Restaurant Offers</div>
<div class="abs hero-sub">Your adventure with affordable taste</div>

<div class="abs search">
  <div class="field">Were To</div>
  <div class="field">Restaurant/Bar Name</div>
  <div class="go">
    <svg width="20" height="20" viewBox="0 0 20 20" fill="none" stroke="#fff" stroke-width="2" stroke-linecap="round"><circle cx="8.5" cy="8.5" r="6"/><path d="M13 13l5 5"/></svg>
  </div>
</div>

<!-- businesses -->
<div class="abs h-section" style="top:770px">Find the Best Businesses in Town</div>

<div class="abs cat" style="left:217px">
  <div class="photo" role="img" aria-label="Friends laughing and sharing dinner in a restaurant" style="background:linear-gradient(160deg,#b98a5c,#6a4630 60%,#3c2a20)"></div>
  <div class="label">Restaurant</div>
</div>
<div class="abs cat" style="left:477px">
  <div class="photo" role="img" aria-label="Group of diners at a long candle-lit table" style="background:linear-gradient(160deg,#3a2718,#6e4a2a 55%,#2a1c12)"></div>
  <div class="label">Diners &amp; Drinkers</div>
</div>
<div class="abs cat" style="left:738px">
  <div class="photo" role="img" aria-label="Warmly lit restaurant and bar interior" style="background:linear-gradient(160deg,#c9c2b4,#a36a3c 55%,#4a3020)"></div>
  <div class="label">Restaurant/Bar</div>
</div>

<div class="abs dot" style="left:574px"></div>
<div class="abs dot on" style="left:593px"></div>
<div class="abs dot" style="left:616px"></div>

<!-- restaurants -->
<div class="abs h-section" style="top:1217px">Find the Best Restaurant in Town</div>

<div class="abs rest" style="left:160px;top:1290px">
  <div class="photo" role="img" aria-label="Couple dining together at a restaurant table" style="background:linear-gradient(150deg,#8a6a4a,#5a4a3c 50%,#2e2a28)"></div>
  <div class="fav"><svg width="16" height="15" viewBox="0 0 24 22" fill="none" stroke="#fff" stroke-width="2.2"><path d="M12 20S2 13.5 2 7a5 5 0 0 1 10-1 5 5 0 0 1 10 1c0 6.5-10 13-10 13z"/></svg></div>
  <div class="name">Restaurant Name</div>
  <div class="desc">Lorem Ipsum is simply dummy text of the printing and typesetting</div>
  <div class="opened">Opened 4 weeks ago</div>
</div>
<div class="abs rest" style="left:461px;top:1290px">
  <div class="photo" role="img" aria-label="Women enjoying burgers at a restaurant" style="background:linear-gradient(150deg,#6a3a24,#8a5a3a 45%,#4a5a78)"></div>
  <div class="fav"><svg width="16" height="15" viewBox="0 0 24 22" fill="none" stroke="#fff" stroke-width="2.2"><path d="M12 20S2 13.5 2 7a5 5 0 0 1 10-1 5 5 0 0 1 10 1c0 6.5-10 13-10 13z"/></svg></div>
  <div class="name">Restaurant Name</div>
  <div class="desc">Lorem Ipsum is simply dummy text of the printing and typesetting</div>
  <div class="opened">Opened 4 weeks ago</div>
</div>
<div class="abs rest" style="left:762px;top:1290px">
  <div class="photo" role="img" aria-label="Waiter serving plates to a group in a bright restaurant" style="background:linear-gradient(150deg,#9a8a7a,#c8c2ba 50%,#6a5a4a)"></div>
  <div class="fav"><svg width="16" height="15" viewBox="0 0 24 22" fill="none" stroke="#fff" stroke-width="2.2"><path d="M12 20S2 13.5 2 7a5 5 0 0 1 10-1 5 5 0 0 1 10 1c0 6.5-10 13-10 13z"/></svg></div>
  <div class="name">Restaurant Name</div>
  <div class="desc">Lorem Ipsum is simply dummy text of the printing and typesetting</div>
  <div class="opened">Opened 4 weeks ago</div>
</div>

<div class="abs rest" style="left:160px;top:1656px">
  <div class="photo" role="img" aria-label="Couple dining together at a restaurant table" style="background:linear-gradient(150deg,#8a6a4a,#5a4a3c 50%,#2e2a28)"></div>
  <div class="fav"><svg width="16" height="15" viewBox="0 0 24 22" fill="none" stroke="#fff" stroke-width="2.2"><path d="M12 20S2 13.5 2 7a5 5 0 0 1 10-1 5 5 0 0 1 10 1c0 6.5-10 13-10 13z"/></svg></div>
  <div class="name">Restaurant Name</div>
  <div class="desc">Lorem Ipsum is simply dummy text of the printing and typesetting</div>
  <div class="opened">Opened 4 weeks ago</div>
</div>
<div class="abs rest" style="left:461px;top:1656px">
  <div class="photo" role="img" aria-label="Table set with wine glasses, juice and a plated dish" style="background:linear-gradient(150deg,#d8a040,#e8d8c0 50%,#b89070)"></div>
  <div class="fav"><svg width="16" height="15" viewBox="0 0 24 22" fill="none" stroke="#fff" stroke-width="2.2"><path d="M12 20S2 13.5 2 7a5 5 0 0 1 10-1 5 5 0 0 1 10 1c0 6.5-10 13-10 13z"/></svg></div>
  <div class="name">Restaurant Name</div>
  <div class="desc">Lorem Ipsum is simply dummy text of the printing and typesetting</div>
  <div class="opened">Opened 4 weeks ago</div>
</div>
<div class="abs rest" style="left:762px;top:1656px">
  <div class="photo" role="img" aria-label="Couple dining together at a restaurant table" style="background:linear-gradient(150deg,#8a6a4a,#5a4a3c 50%,#2e2a28)"></div>
  <div class="fav"><svg width="16" height="15" viewBox="0 0 24 22" fill="none" stroke="#fff" stroke-width="2.2"><path d="M12 20S2 13.5 2 7a5 5 0 0 1 10-1 5 5 0 0 1 10 1c0 6.5-10 13-10 13z"/></svg></div>
  <div class="name">Restaurant Name</div>
  <div class="desc">Lorem Ipsum is simply dummy text of the printing and typesetting</div>
  <div class="opened">Opened 4 weeks ago</div>
</div>

<!-- blog -->
<div class="abs h-section" style="top:2085px">Latest Blog</div>

<div class="abs post" style="left:159px;top:2165px">
  <div class="photo" role="img" aria-label="Table with wine glasses, juice and a plated dish" style="background:linear-gradient(150deg,#d8a040,#e8d8c0 50%,#b89070)"><div class="date">30<br>Nov</div></div>
  <div class="meta">By Admin<span>.</span><span style="margin-left:12px">2 Comments</span></div>
  <div class="title">Lorem Ipsum is simply dummy text of the printing</div>
  <div class="excerpt">There are many variations of passages of available but majority have alteration</div>
  <div class="more">Read More</div>
</div>
<div class="abs post" style="left:461px;top:2165px">
  <div class="photo" role="img" aria-label="Hands passing a bowl of salad across a wooden table" style="background:linear-gradient(150deg,#3a4048,#9a6a40 50%,#c8b090)"><div class="date">30<br>Nov</div></div>
  <div class="meta">By Admin<span>.</span><span style="margin-left:12px">2 Comments</span></div>
  <div class="title">Lorem Ipsum is simply dummy text of the printing</div>
  <div class="excerpt">There are many variations of passages of available but majority have alteration</div>
  <div class="more">Read More</div>
</div>
<div class="abs post" style="left:763px;top:2165px">
  <div class="photo" role="img" aria-label="Menu board with cutlery and vegetables on a rustic table" style="background:linear-gradient(150deg,#5a4030,#3a3028 50%,#6a3a28)"><div class="date">30<br>Nov</div></div>
  <div class="meta">By Admin<span>.</span><span style="margin-left:12px">2 Comments</span></div>
  <div class="title">Lorem Ipsum is simply dummy text of the printing</div>
  <div class="excerpt">There are many variations of passages of available but majority have alteration</div>
  <div class="more">Read More</div>
</div>

<!-- footer -->
<div class="abs footer"></div>
<div class="abs f-brand">NomiDeals</div>
<div class="abs social" style="left:148px"></div>
<div class="abs social" style="left:179px"></div>
<div class="abs social" style="left:216px"></div>

<div class="abs f-head" style="left:350px;top:2697px">Contact Us</div>
<svg class="abs" style="left:350px;top:2741px" width="14" height="18" viewBox="0 0 14 18" fill="none" stroke="#fff" stroke-width="1.4"><path d="M7 17s6-6 6-10A6 6 0 0 0 1 7c0 4 6 10 6 10z"/><circle cx="7" cy="7" r="2.2"/></svg>
<div class="abs f-text" style="left:379px;top:2740px">482 Larkfield Avenue #12<br>Brookvale 20419</div>
<svg class="abs" style="left:349px;top:2794px" width="18" height="18" viewBox="0 0 24 24" fill="#fff"><path d="M6.6 10.8a15 15 0 0 0 6.6 6.6l2.2-2.2a1 1 0 0 1 1-.25 11.4 11.4 0 0 0 3.6.57 1 1 0 0 1 1 1V20a1 1 0 0 1-1 1A17 17 0 0 1 3 4a1 1 0 0 1 1-1h3.5a1 1 0 0 1 1 1c0 1.25.2 2.45.57 3.6a1 1 0 0 1-.25 1z"/></svg>
<div class="abs f-text" style="left:379px;top:2793px">(555) 014-2290</div>
<svg class="abs" style="left:349px;top:2832px" width="18" height="14" viewBox="0 0 18 14" fill="#fff"><path d="M0 0h18v14H0z" fill="#fff"/><path d="M0 0l9 7 9-7" fill="none" stroke="#414141" stroke-width="1.4"/></svg>
<div class="abs f-text" style="left:379px;top:2830px">hello@nomideals.net</div>

<div class="abs f-head" style="left:616px;top:2697px">Company</div>
<ul class="abs f-links" style="left:616px;top:2733px">
  <li>Home</li><li>Diners &amp; Drinkers</li><li>Restaurant/Bar</li><li>Services</li><li>Blog</li><li>Contact Us</li>
</ul>

<div class="abs f-head" style="left:805px;top:2699px">Stil have questions?</div>
<div class="abs f-text" style="left:805px;top:2737px;width:280px;line-height:22px;font-size:14px">Contact us usig this form. A repesenta-tive will aswer your questions as soon as possible.</div>
<div class="abs cta">Get In Touch
  <svg width="22" height="10" viewBox="0 0 22 10" fill="none" stroke="#fff" stroke-width="1.5"><path d="M0 5h20M16 1l4 4-4 4"/></svg>
</div>

<div class="abs footer-bar"></div>
<div class="abs copy">Copyright 2020 NomiDeals. All Rights Reserved.</div>
<div class="abs legal" style="left:837px">Privacy Policy</div>
<div class="abs legal" style="left:953px">Terms Of Services</div>

</body>
</html>
```